Eye-catching & Glamorous Labels for Skincare Bottles & Jars

We need new labels designed for our product range as we have been dormant for a few years and are now rebranding Velora Grace - Kindly Made Skincare. The label sizes are defined in the attached word document. All products have either a bright silver or a matte silver lid pump/spray so please keep this in mind.

We are open to colours and invite you to create bright trendy labels which are coordinated with the logo attached. The logo is not of any specific colour so dark on light, light on dark, tone on tone - we like purple / duck egg blue / turquoise WITH matte silver, however stronger colours like navy plus maroon with matte silver is also a strong favourite. If you feel inspired by a colour you think would be appropriate to Velora Grace please feel free to have a go.

A front section for product information is required and the back should include relevant details ie ingredients, company info, and a note that there has been no testing on animals.

The serum bottle will require a front and back label on a clear label in a pale colour to coordinate with the rest of the range. Size for this label is 35mm top edge, 25mm bottom edge, height 45mm - I have attached a picture of the serum bottle as they were originally pad printed. Please don't hesitate to contact me for any further information. Good luck!

Target Market(s)

Educated professional women 30-45 who are regular skincare users and looking for beautiful skincare products without animal derived ingredients and animal testing

Industry/Entity Type

Skin Care Product

Font styles to use
Serif
Sans Serif
Decorative
Script

Colors

Designer to choose colors to be used in the design.

Requirements
Must have
• Velora Grace Logo - eye catching design - not too busy or cramped.
Nice to have
• Is it possible to create a background pattern using a very small image of the logo? Just a thought.

```html
<!DOCTYPE html>
<html lang="en">
<head>
<meta charset="utf-8">
<title>Velora Grace – Oil Serum Label</title>
<link href="https://fonts.googleapis.com/css2?family=Arimo:wght@400;700&family=Allura&display=swap" rel="stylesheet">
<style>
  :root {
    --backdrop: #8c8c8e;
    --label: #ffffff;
    --turquoise: #38b3c4;
    --duck-egg: #a9dbe3;
    --leaf-pale: #d9eff3;
    --ink: #222222;
    --ink-soft: #444444;
    --pill: #1e1b1b;
  }
  * { margin: 0; padding: 0; box-sizing: border-box; }
  html, body { width: 1200px; height: 1200px; overflow: hidden; }
  body {
    background: var(--backdrop);
    display: flex;
    align-items: center;
    justify-content: center;
    font-family: "Arimo", Arial, sans-serif;
  }
  .serum-label {
    position: relative;
    width: 600px;
    height: 800px;
    background: var(--label);
    clip-path: polygon(0 0, 100% 0, 88% 100%, 12% 100%);
    text-align: center;
    color: var(--ink);
  }
  .corner-decor {
    position: absolute;
    background: radial-gradient(circle at 30% 30%, var(--leaf-pale), rgba(255,255,255,0) 70%);
  }
  .corner-decor--left { top: 0; left: 0; width: 200px; height: 220px; }
  .corner-decor--right { top: 90px; right: 0; width: 80px; height: 110px;
    background: radial-gradient(circle at 80% 50%, var(--leaf-pale), rgba(255,255,255,0) 70%); }
  .brand-mark {
    position: absolute;
    top: 98px; left: 0; right: 0;
    font-size: 26px;
    font-weight: 700;
    color: var(--ink);
  }
  .brand-name {
    position: absolute;
    top: 240px; left: 0; right: 0;
    font-size: 44px;
    font-weight: 700;
    letter-spacing: 0.5px;
    color: var(--turquoise);
  }
  .brand-tagline {
    position: absolute;
    top: 296px; left: 0; right: 0;
    font-size: 21px;
    letter-spacing: 0.8px;
    color: #555;
  }
  .brand-rule {
    position: absolute;
    top: 326px; left: 50%;
    width: 290px; height: 2px;
    margin-left: -145px;
    background: var(--duck-egg);
  }
  .range-pill {
    position: absolute;
    top: 378px; left: 50%;
    width: 396px; height: 60px;
    margin-left: -198px;
    background: var(--pill);
    border-radius: 30px;
    color: #fff;
    font-family: "Allura", cursive;
    font-size: 42px;
    line-height: 60px;
  }
  .product-type {
    position: absolute;
    top: 460px; left: 0; right: 0;
    font-size: 27px; font-weight: 700;
  }
  .product-name {
    position: absolute;
    top: 503px; left: 0; right: 0;
    font-size: 21px; letter-spacing: 0.6px; color: var(--ink-soft);
  }
  .animal-note {
    position: absolute;
    top: 541px; left: 0; right: 0;
    font-size: 18px; letter-spacing: 0.2px; color: var(--ink-soft);
  }
  .volume {
    position: absolute;
    top: 574px; left: 0; right: 0;
    display: flex; align-items: center; justify-content: center; gap: 8px;
    font-size: 21px; font-weight: 700;
  }
  .volume-line { width: 55px; height: 2px; background: var(--turquoise); }
  .volume-dot { width: 5px; height: 5px; border-radius: 50%; background: var(--turquoise); }
  .lotus-art {
    position: absolute;
    bottom: 0; left: 50%;
    width: 320px; height: 180px;
    margin-left: -160px;
    background: linear-gradient(180deg, rgba(169,219,227,0) 0%, var(--duck-egg) 45%, var(--turquoise) 100%);
  }
</style>
</head>
<body>
  <main class="serum-label">
    <div class="corner-decor corner-decor--left" role="img" aria-label="Pale turquoise leaf decoration"></div>
    <div class="corner-decor corner-decor--right" role="img" aria-label="Pale turquoise leaf decoration"></div>
    <div class="brand-mark">Velora Grace</div>
    <h1 class="brand-name">VELORA GRACE</h1>
    <p class="brand-tagline">KINDLY MADE SKINCARE</p>
    <div class="brand-rule"></div>
    <div class="range-pill">Ageless Reserve</div>
    <p class="product-type">OIL SERUM</p>
    <p class="product-name">SILKEN RITUAL</p>
    <p class="animal-note">THERE HAS BEEN NO TESTING ON ANIMALS</p>
    <div class="volume">
      <span class="volume-line"></span><span class="volume-dot"></span>
      30ml
      <span class="volume-dot"></span><span class="volume-line"></span>
    </div>
    <div class="lotus-art" role="img" aria-label="Turquoise lotus flower illustration"></div>
  </main>
</body>
</html>
```